Business Card for Academic Coach

I need a business card designed for me - a private tutor/academic coach.

Glen Mabery
Academic Coach
AB Pellwood University, 1994 Cum Laude
Phone: 404-555-0187
glenrmabery@tutormail-example.com

Subjects
QET and BRT
Math, Physics, Writing

```html
<!DOCTYPE html>
<html lang="en">
<head>
<meta charset="utf-8">
<title>Glen Mabery – Academic Coach Business Card</title>
<link rel="stylesheet" href="https://fonts.googleapis.com/css2?family=Tinos&display=swap">
<style>
  :root {
    --navy: #0b3f7e;
    --sky: #1a8fef;
    --ink: #111111;
    --paper: #ffffff;
    --stage: #ffffff;
    --sketch-a: #5b79b0;
    --sketch-b: #dfe6f3;
  }
  html, body {
    margin: 0;
    padding: 0;
    width: 1200px;
    height: 900px;
    overflow: hidden;
    background: var(--stage);
  }
  .canvas {
    position: relative;
    width: 1200px;
    height: 900px;
    font-family: "Tinos", "Times New Roman", serif;
    color: var(--ink);
  }
  .card {
    position: absolute;
    background: var(--paper);
    overflow: hidden;
    box-shadow: 0 0 0 1px #d8d8d8;
  }
  .card--front { left: 35px; top: 82px; width: 587px; height: 336px; }
  .card--back  { left: 55px; top: 517px; width: 588px; height: 335px; }

  .block { position: absolute; }
  .block--navy { background: var(--navy); }
  .block--sky  { background: var(--sky); }

  .books-art {
    position: absolute;
    background: radial-gradient(ellipse at 50% 50%, var(--sketch-a) 0%, #9fb2d4 40%, var(--sketch-b) 75%, rgba(255,255,255,0) 100%);
    opacity: 0.55;
  }

  .name {
    position: absolute;
    margin: 0;
    left: 0; right: 0;
    text-align: center;
    font-weight: 400;
    font-size: 48px;
    line-height: 1;
    color: var(--sky);
    text-shadow: 1px 2px 2px rgba(0,0,0,0.35);
  }
  .role {
    position: absolute;
    margin: 0;
    font-size: 21px;
    line-height: 1;
  }
  .contact {
    position: absolute;
    margin: 0;
    font-size: 22px;
    line-height: 1;
    white-space: nowrap;
  }
  .subjects-title {
    position: absolute;
    margin: 0;
    font-weight: 400;
    font-size: 36px;
    line-height: 1;
    color: var(--sky);
    text-shadow: 1px 2px 2px rgba(0,0,0,0.3);
  }
  .subject-line {
    position: absolute;
    margin: 0;
    font-size: 23px;
    line-height: 1;
    white-space: nowrap;
  }
</style>
</head>
<body>
<main class="canvas">

  <section class="card card--front" aria-label="Business card front">
    <div class="block block--navy" style="left:0; top:0; width:252px; height:101px;"></div>
    <div class="block block--sky" style="left:0; top:101px; width:587px; height:6px;"></div>
    <div class="books-art" role="img" aria-label="Sketched stack of books in blue" style="left:10px; top:110px; width:205px; height:205px;"></div>

    <h1 class="name" style="top:24px; left:60px;">Glen Mabery</h1>
    <p class="role" style="left:265px; top:71px;">Academic Coach</p>

    <p class="contact" style="left:153px; top:151px;">AB Pellwood University, 1994 Cum Laude</p>
    <p class="contact" style="left:210px; top:177px;">Phone: 404-555-0187</p>
    <p class="contact" style="left:198px; top:205px;">glenrmabery@tutormail-example.com</p>

    <div class="block block--navy" style="left:0; top:315px; width:403px; height:10px;"></div>
    <div class="block block--sky" style="left:338px; top:325px; width:249px; height:11px;"></div>
  </section>

  <section class="card card--back" aria-label="Business card back">
    <div class="block block--navy" style="left:0; top:0; width:588px; height:98px;"></div>
    <div class="block block--sky" style="left:0; top:98px; width:588px; height:6px;"></div>
    <div class="books-art" role="img" aria-label="Sketched stack of books in blue" style="left:40px; top:63px; width:245px; height:250px;"></div>

    <h2 class="subjects-title" style="left:345px; top:124px;">Subjects</h2>
    <p class="subject-line" style="left:337px; top:165px;">QET and BRT</p>
    <p class="subject-line" style="left:313px; top:198px;">Math, Physics, Writing</p>

    <div class="block block--navy" style="left:0; top:314px; width:405px; height:12px;"></div>
    <div class="block block--sky" style="left:294px; top:326px; width:294px; height:9px;"></div>
  </section>

</main>
</body>
</html>
```